Olive Oil label for bottle 0.5l approx. 10x12 cm

I am running a Spa hotel in Bavaria (logo attached) and my family lives in Greece (Bavarian and Greek flag have the same colors). They produce organic olive oil first cold pressed extra virgin. I would need a label for 0,5 liter bottles to reach them out to my guests and they should see the high quality of the olive oil and the family connection Spa-hotel Bavaria to family in Greece. The name of the family is Morvatek, the hotel is called Tannegg, the olive oil comes from Greece/Argolis/Kranidi. The name of the small olive company is Kerano Hawks. There should be a space for the best before date and the organic control number (handwritten) . The hotel logo is not mandatory. Should look nice 😉

```html
<!DOCTYPE html>
<html lang="en">
<head>
<meta charset="utf-8">
<title>Tannegg Olive Oil – Bottle Labels</title>
<link rel="stylesheet" href="https://fonts.googleapis.com/css2?family=Arimo:wght@400;700&family=Oswald:wght@300&display=swap">
<style>
  :root {
    --backdrop: #dadada;
    --paper: #f7f7f7;
    --teal: #7f9896;
    --teal-dark: #6f8a88;
    --teal-light: #a2b5b3;
    --white: #ffffff;
    --flag-blue: #2f7cc6;
    --olive-light: #c9c83a;
    --olive-mid: #9aa72c;
    --leaf: #4f7a2a;
  }
  * { margin: 0; padding: 0; box-sizing: border-box; }
  html, body { width: 1200px; height: 848px; overflow: hidden; background: var(--backdrop); }
  .canvas { position: relative; width: 1200px; height: 848px; }

  .label {
    position: absolute; top: 55px; width: 306px; height: 738px;
    background: var(--paper); overflow: hidden;
    font-family: "Arimo", Arial, sans-serif;
  }
  .label--front { left: 189px; }
  .label--back { left: 706px; }

  .label__band {
    position: absolute; left: 0; right: 0; top: 450px; bottom: 0;
    background: linear-gradient(90deg, var(--teal-dark) 0%, var(--teal-light) 50%, var(--teal-dark) 100%);
  }
  .label__frame { position: absolute; inset: 0; width: 100%; height: 100%; }

  .olives {
    position: absolute; left: 40px; top: 372px; width: 226px; height: 118px;
    border-radius: 50% 50% 46% 46%;
    background: radial-gradient(ellipse at 50% 60%, var(--olive-light) 0%, var(--olive-mid) 45%, rgba(79,122,42,0.55) 75%, rgba(79,122,42,0) 100%);
  }

  .brand-name {
    position: absolute; left: 0; right: 0; text-align: center;
    color: var(--teal); font-weight: 400; letter-spacing: 1px;
  }
  .label--front .brand-name { top: 190px; font-size: 44px; }
  .label--back .brand-mark {
    position: absolute; left: 103px; top: 150px; width: 100px; height: 100px;
    border: 3px solid var(--teal); border-radius: 50%;
  }
  .label--back .brand-name { top: 262px; font-size: 30px; }

  .product-title {
    position: absolute; left: 0; right: 0; top: 520px; text-align: center;
    font-family: "Oswald", "Arial Narrow", sans-serif; font-weight: 300;
    font-size: 60px; line-height: 1; color: var(--white); letter-spacing: 0.5px;
  }
  .product-type {
    position: absolute; left: 39px; width: 228px; top: 579px; height: 31px;
    background: var(--white); border: 1.5px solid var(--teal);
    outline: 1.5px solid var(--white); outline-offset: 2px;
    color: var(--teal); font-size: 18px; line-height: 28px; text-align: center; letter-spacing: 0.5px;
  }
  .product-process {
    position: absolute; left: 0; right: 0; top: 619px; text-align: center;
    color: var(--white); font-size: 11.5px; letter-spacing: 0.3px;
  }
  .product-volume {
    position: absolute; left: 0; right: 0; top: 654px; text-align: center;
    color: var(--white); font-size: 18px; font-weight: 700;
  }

  .origin-flag { position: absolute; left: 101px; top: 527px; width: 103px; height: 68px; }
  .origin-text, .best-before {
    position: absolute; left: 0; right: 0; text-align: center;
    color: var(--white); font-size: 11px; line-height: 14px; letter-spacing: 0.3px;
  }
  .origin-text { top: 601px; }
  .best-before { top: 639px; line-height: 15px; }
</style>
</head>
<body>
<main class="canvas">

  <!-- Front label -->
  <section class="label label--front">
    <div class="label__band"></div>
    <svg class="label__frame" viewBox="0 0 340 820" aria-hidden="true">
      <defs>
        <linearGradient id="frameInkFront" gradientUnits="userSpaceOnUse" x1="0" y1="0" x2="0" y2="820">
          <stop offset="0.609" stop-color="#7f9896"/>
          <stop offset="0.609" stop-color="#ffffff"/>
        </linearGradient>
      </defs>
      <g fill="none" stroke="url(#frameInkFront)" stroke-width="2">
        <path d="M40 18 H300 A14 14 0 0 0 322 40 V780 A14 14 0 0 0 300 802 H40 A14 14 0 0 0 18 780 V40 A14 14 0 0 0 40 18 Z"/>
        <path d="M44 24 H296 A18 18 0 0 0 316 44 V776 A18 18 0 0 0 296 796 H44 A18 18 0 0 0 24 776 V44 A18 18 0 0 0 44 24 Z" stroke-width="1"/>
        <circle cx="27" cy="27" r="7"/><circle cx="313" cy="27" r="7"/>
        <circle cx="27" cy="793" r="7"/><circle cx="313" cy="793" r="7"/>
      </g>
      <g fill="url(#frameInkFront)">
        <circle cx="27" cy="27" r="3"/><circle cx="313" cy="27" r="3"/>
        <circle cx="27" cy="793" r="3"/><circle cx="313" cy="793" r="3"/>
      </g>
    </svg>
    <div class="brand-name">Tannegg</div>
    <div class="olives" role="img" aria-label="Photograph of green olives with olive leaves"></div>
    <h1 class="product-title">OLIVE OIL</h1>
    <div class="product-type">ORGANIC OLIVE OIL</div>
    <p class="product-process">FIRST COLD PRESSED EXTRA VIRGIN</p>
    <p class="product-volume">0.5 L</p>
  </section>

  <!-- Back label -->
  <section class="label label--back">
    <div class="label__band"></div>
    <svg class="label__frame" viewBox="0 0 340 820" aria-hidden="true">
      <defs>
        <linearGradient id="frameInkBack" gradientUnits="userSpaceOnUse" x1="0" y1="0" x2="0" y2="820">
          <stop offset="0.609" stop-color="#7f9896"/>
          <stop offset="0.609" stop-color="#ffffff"/>
        </linearGradient>
      </defs>
      <g fill="none" stroke="url(#frameInkBack)" stroke-width="2">
        <path d="M40 18 H300 A14 14 0 0 0 322 40 V780 A14 14 0 0 0 300 802 H40 A14 14 0 0 0 18 780 V40 A14 14 0 0 0 40 18 Z"/>
        <path d="M44 24 H296 A18 18 0 0 0 316 44 V776 A18 18 0 0 0 296 796 H44 A18 18 0 0 0 24 776 V44 A18 18 0 0 0 44 24 Z" stroke-width="1"/>
        <circle cx="27" cy="27" r="7"/><circle cx="313" cy="27" r="7"/>
        <circle cx="27" cy="793" r="7"/><circle cx="313" cy="793" r="7"/>
      </g>
      <g fill="url(#frameInkBack)">
        <circle cx="27" cy="27" r="3"/><circle cx="313" cy="27" r="3"/>
        <circle cx="27" cy="793" r="3"/><circle cx="313" cy="793" r="3"/>
      </g>
    </svg>
    <div class="brand-mark"></div>
    <div class="brand-name">Tannegg</div>
    <div class="olives" role="img" aria-label="Photograph of green olives with olive leaves"></div>
    <svg class="origin-flag" viewBox="0 0 27 18" role="img" aria-label="Flag of Greece">
      <rect width="27" height="18" fill="#ffffff"/>
      <g fill="#2f7cc6">
        <rect y="0" width="27" height="2"/><rect y="4" width="27" height="2"/>
        <rect y="8" width="27" height="2"/><rect y="12" width="27" height="2"/>
        <rect y="16" width="27" height="2"/>
        <rect width="10" height="10"/>
      </g>
      <g fill="#ffffff"><rect x="4" width="2" height="10"/><rect y="4" width="10" height="2"/></g>
    </svg>
    <p class="origin-text">MADE IN GREECE<br>ARGOLIS • KRANIDI</p>
    <p class="best-before">THE BEST BEFORE:<br>4.8.2024</p>
  </section>

</main>
</body>
</html>
```